RVK Entertainment

Logo for business card design

Target Market(s)

potential film investors and screenwriters

Industry/Entity Type

Business

Contact Information for Business Card

as shown, website here is a placeholder position

Requirements
Must have
• great visual appeal
Nice to have
• harmony of colors; must evoke spirit of
• U.S.-China cooperation

```html
<!DOCTYPE html>
<html lang="en">
<head>
<meta charset="utf-8">
<title>RVK Entertainment – Business Card</title>
<link rel="stylesheet" href="https://fonts.googleapis.com/css2?family=Open+Sans:wght@400;600&display=swap">
<style>
  :root {
    --page-bg: #f4f4f2;
    --card-brown: #2f1e14;
    --band-gold: #f2b636;
    --mark-red: #d8102f;
    --text-white: #ffffff;
    --text-grey: #b9b1aa;
    --text-dark: #2f1e14;
  }
  * { margin: 0; padding: 0; box-sizing: border-box; }
  html, body {
    width: 1200px; height: 900px; overflow: hidden;
    background: var(--page-bg);
    font-family: "Open Sans", Arial, sans-serif;
  }
  .business-card {
    position: absolute; left: 160px; top: 180px;
    width: 880px; height: 540px;
    background: var(--card-brown);
    box-shadow: 0 6px 24px rgba(0,0,0,0.18);
    overflow: hidden;
  }
  .side-band {
    position: absolute; right: 0; top: 0;
    width: 160px; height: 100%;
    background: var(--band-gold);
  }
  .brand-lockup {
    position: absolute; left: 170px; top: 150px;
    display: flex; align-items: center; gap: 22px;
  }
  .brand-square {
    width: 110px; height: 110px;
    background: var(--mark-red);
  }
  .brand-name {
    color: var(--text-white); font-weight: 600;
    line-height: 1;
  }
  .brand-name .initials { display: block; font-size: 104px; letter-spacing: 4px; }
  .brand-name .descriptor { display: block; font-size: 26px; letter-spacing: 7px; margin-top: 10px; }
  .contact-address {
    position: absolute; left: 0; width: 720px; top: 448px;
    text-align: center; color: var(--text-grey);
    font-size: 17px; line-height: 1.5; font-weight: 400;
  }
  .band-name {
    position: absolute; right: 50px; top: 200px;
    transform-origin: center; transform: rotate(90deg) translateX(0);
    display: flex; align-items: center; gap: 8px;
    color: var(--text-dark); font-weight: 600;
    font-size: 15px; letter-spacing: 2px; white-space: nowrap;
  }
  .band-square { width: 16px; height: 16px; background: var(--text-dark); }
</style>
</head>
<body>
  <section class="business-card" aria-label="RVK Entertainment business card">
    <div class="brand-lockup">
      <span class="brand-square" aria-hidden="true"></span>
      <h1 class="brand-name">
        <span class="initials">RVK</span>
        <span class="descriptor">ENTERTAINMENT</span>
      </h1>
    </div>
    <p class="contact-address">418 Larkin Ave #210, Fair Oaks<br>California 95628 USA website here</p>
    <aside class="side-band">
      <div class="band-name" style="right:-20px;top:120px;">
        <span class="band-square" aria-hidden="true"></span>RVK ENTERTAINMENT
      </div>
    </aside>
  </section>
</body>
</html>
```